Miriams Professional Resume

Pls upgrade to make look more effective and perhaps add α photo on it, both options with photo and without would be great. Thanks very much. I would also like the resume so I can edit as well if I need to down the track.

Target Market(s)

This is my professional resume to make it more effective to potential senior hiring managers,

Colors
f04a50

Requirements
Must have
• Professional look.

```html
<!DOCTYPE html>
<html lang="en">
<head>
<meta charset="utf-8">
<title>Miriams Professional Resume – Page 2</title>
<link href="https://fonts.googleapis.com/css2?family=Tinos:wght@400;700&display=swap" rel="stylesheet">
<style>
  :root {
    --sidebar: #a86062;
    --sidebar-text: #f6eeee;
    --page: #eceeed;
    --ink: #2b2b2b;
    --rule: #a85a5c;
  }
  * { margin: 0; padding: 0; box-sizing: border-box; }
  html, body { width: 850px; height: 1200px; overflow: hidden; }
  body { font-family: "Tinos", "Times New Roman", serif; background: var(--page); }
  .resume { position: relative; width: 850px; height: 1200px; overflow: hidden; background: var(--page); }
  .sidebar { position: absolute; left: 0; top: 0; width: 362px; height: 1200px; background: var(--sidebar); color: var(--sidebar-text); }
  .rosette { position: absolute; left: 55px; top: 370px; width: 650px; height: 640px; }
  .block { position: absolute; font-size: 15.6px; line-height: 18.3px; }
  .sidebar .block { left: 35px; width: 310px; }
  .heading { font-weight: 700; font-size: 15.6px; line-height: 19px; }
  .main { position: absolute; left: 0; top: 0; width: 850px; height: 1200px; color: var(--ink); }
  .main .block { left: 407px; width: 405px; }
  .duties { list-style: none; }
  .duties li { position: relative; padding-left: 9px; }
  .duties li::before { content: "•"; position: absolute; left: 0; }
  .role-title { font-weight: 700; font-size: 15.6px; line-height: 19px; }
  .rule { position: absolute; height: 2px; background: var(--rule); }
</style>
</head>
<body>
<div class="resume">
  <aside class="sidebar">
    <div class="block heading" style="top:52px">EDUCATION</div>
    <div class="block" style="top:89px">Masters in Strategic Organisational Development University of Northfield, Australia December 2011 to December 2017</div>
    <div class="block" style="top:162px">Management in Human Resources Certificate – Graduated with Distinction Pacific Coast University Extension Program, USA June 2003 – November 2006</div>
    <div class="block" style="top:253px">Bachelor of Business in Tourism Management Southbank University, Australia January 1992 to December 1996</div>
    <div class="block heading" style="top:345px">PROFESSIONAL MEMBERSHIPS</div>
    <div class="block" style="top:382px">Member of Singapore People Practice Institute, 104 5521 2020 Member of Australian People Management Institute, 381562.</div>
    <div class="block heading" style="top:492px">CURRENT COURSES COMPLETED, 2020</div>
    <div class="block" style="top:549px">Singapore Employment Legislation and Industrial Relations, SPPI, 2020.</div>
    <div class="block" style="top:604px">Human Resource Analytics and Insights, SPPI, 2020.</div>
    <div class="block" style="top:678px"><span class="heading">NetLink Profile:</span><br>https://www.netlink.com/in/miriam-holt-</div>
  </aside>

  <svg class="rosette" viewBox="0 0 650 640" role="img" aria-label="Faint decorative guilloche rosette behind the page">
    <defs>
      <radialGradient id="rosetteGlow" cx="50%" cy="50%" r="50%">
        <stop offset="0%" stop-color="#8a4446" stop-opacity="0"/>
        <stop offset="55%" stop-color="#8a4446" stop-opacity="0.10"/>
        <stop offset="100%" stop-color="#8a4446" stop-opacity="0"/>
      </radialGradient>
    </defs>
    <ellipse cx="325" cy="320" rx="320" ry="315" fill="url(#rosetteGlow)"/>
  </svg>

  <main class="main">
    <ul class="block duties" style="top:40px">
      <li>Recruit new Service Provider contracts with Brightfizz, Crispins, Goldarch Burgers and STAG.</li>
      <li>Project P + L Financial Management to $ 1.2m SG</li>
      <li>Workforce Planning on Technical Field Projects for Brightfizz and Crispins for resources across NSW, QLD, VIC and SA for &gt; 200 services equipment assets, 400 + operational field services performed per month.</li>
      <li>Focused on quality service results, delivering a positive customer service experience.</li>
    </ul>

    <div class="block role-title" style="top:223px">Westmere College, Director Career Services. USA, October 2003 to December 2007</div>
    <ul class="block duties" style="top:280px">
      <li>Brand expansion, Business Development, Marketing of Westmere College into San Francisco, Sacramento, Fremont, Santa Clara and the Bay Area.</li>
      <li>Built out the department from scratch, developed strategies, process and service standards.</li>
      <li>HR Strategy and Human Resource Operations: Recruitment, Job Placement, Performance Management, HR Policy, Training and Development.</li>
      <li>Graduate Program Placement for 700 + Medical graduates, MA, LVN and RN Program.</li>
      <li>Acquired new accounts from multiple hospitals and medical centres across the San Francisco Bay Area.</li>
      <li>Project Management with Senior Leadership Team for Board of Private Education Accreditation Business Goal, engagement and contracts for preceptorships sites to facilitate L &amp; D.</li>
      <li>Awarded 2005 - Employee of the Year</li>
      <li>Account Management: Harbor Health Group, Oakridge Medical Centre, Valley View Medical Centre and Department of Service Veterans.</li>
    </ul>

    <div class="rule" style="left:408px; top:668px; width:397px"></div>
    <div class="block role-title" style="top:700px">Recruitment Consultant, Calder International, Health Care and IT Industry Australia, July 2002 to April 2003</div>
    <div class="rule" style="left:408px; top:765px; width:397px"></div>
    <div class="block role-title" style="top:795px">Recruitment Consultant, Netspan, IT Industry Australia, July 2001 to May 2002</div>
    <div class="rule" style="left:408px; top:859px; width:397px"></div>
    <div class="block role-title" style="top:890px">Sales and IT Sourcer, Corvex Systems, IT Industry Australia, April 2000 to April 2001</div>
    <div class="rule" style="left:500px; top:959px; width:214px"></div>
  </main>
</div>
</body>
</html>
```